Psychotherapy Website - Based in London

I am a newly trained psychotherapist and need a new website for www.rosalindfaber.co.uk.

I offer therapy for addiction, relationships, trauma and many other issues people face in their lives.

I want the website to be welcoming, gentle, feminine and for people to feel safe.

I do not like a page site that scrolls through sections, rather each page should be separate. Here some examples that i like. Sectional rather than scrolled.

https://www.hettiemarsh.com/
https://www.thequietwardrooms.com/

The imagery should be around pink using the flower in the logo / wording and around the site:

Here is a link to the flower for ideas:
https://www.pictofind.net/search?q=pink+gerbera&rlz=2D4KQTW_en-GBGB415GB415&source=lnms&tbm=isch&sa=X&ved=7cvQRtrk482h3PxZTuKLmeNBwXW_1AtXpVlKDbOQBmFLB&biw=1500&bih=889&dpr=2

RosalindFaber
Compassionate Psychotherapy

Is the logo and subheader for the website. Please use a typeface for the name that is appealing and professional.

Type face similar NOT EXLUSIVLY - JUST AN IDEA like this:
https://glowtonicstudio.com/

Basic business card i created as a rough idea below.

I have also added the website copy.

The headers are

Homepage
About Me
Therapy
Common Questions
Blog
Contact Me

Target Market(s)

Clients who are dealing with stress, trauma, pain, addiction

Industry/Entity Type

Therapy and Psychology

Coding

Coded - Design and coding required

Number of Pages Required

5+ page

Font styles to use
Serif
Sans Serif
Script

Colors
0054AA
0677BA
7BADD7
CADEEF
E8F1F8
0094D4
00A9DD
6FCCEA
C7EBF8
E9F6FB
E54698
E96AAD
F1A4CE
F9D9EA
FCEFF6

Requirements
Must have
• Pink Gerbera Flower integrated into design
Nice to have
• Images but not to stock imagery. Needs to look authentic and natural
Should not have
• Stock images of people. Images are important but needs to feel REAL

```html
<!DOCTYPE html>
<html lang="en">
<head>
<meta charset="utf-8">
<title>RosalindFaber – Compassionate Psychotherapy</title>
<link rel="stylesheet" href="https://fonts.googleapis.com/css2?family=Libre+Caslon+Text:wght@400;700&family=Roboto:wght@400;500;700&display=swap">
<style>
:root{
  --navy:#0054AA;
  --blue:#0677BA;
  --help:#1370B6;
  --news:#0B5EA6;
  --footer:#1068B3;
  --sky:#7BADD7;
  --pink:#E54698;
  --pink-mid:#F1A4CE;
  --pink-soft:#F9D9EA;
  --ink:#1d1d1d;
  --grey-bg:#E3E3E3;
  --field:#C9C9C9;
  --hero-dark:#1B2A33;
  --hero-teal:#3E6663;
  --white:#ffffff;
}
*{margin:0;padding:0;box-sizing:border-box}
html,body{width:1200px;height:4808px;overflow:hidden;background:#fff}
body{position:relative;font-family:"Roboto",Arial,sans-serif;color:var(--ink)}
.serif{font-family:"Libre Caslon Text",Georgia,serif}
section,header,footer{position:absolute;left:0;width:1200px}
.abs{position:absolute}
.ph{position:absolute}

/* hero */
.hero{top:0;height:680px;overflow:hidden}
.hero-bg{position:absolute;inset:0;background:linear-gradient(100deg,var(--hero-dark) 0%,#243A42 45%,var(--hero-teal) 70%,#22343C 100%)}
.nav a{position:absolute;top:32px;color:#fff;font-size:17px;text-decoration:none}
.nav .active::after{content:"";position:absolute;left:0;right:0;bottom:-9px;height:2px;background:#fff}
.brand-text{position:absolute;left:62px;top:36px;color:#fff;font-size:22px;font-weight:500}
.contact-btn{position:absolute;left:1009px;top:26px;width:141px;height:37px;border-radius:19px;background:#fff;color:var(--ink);font-size:15px;font-weight:500;display:flex;align-items:center;justify-content:center}
.hero-title{position:absolute;left:0;width:660px;top:310px;text-align:center;color:#fff}
.hero-title h1{font-size:58px;font-weight:700;line-height:1.1}
.hero-title p{font-size:31px;font-weight:700;margin-top:2px}

/* about */
.about{top:680px;height:600px}
.about h2{position:absolute;left:646px;top:150px;font-size:32px;font-weight:700;white-space:nowrap}
.about h2 span,.therapy h2 span{color:var(--blue)}
.about .copy{position:absolute;left:646px;top:222px;width:405px;font-size:13.4px;line-height:1.45}
.about .copy p+p{margin-top:17px}
.frame{position:absolute;border:1.5px solid #bdbdbd}
.tint{position:absolute;background:#E6E6E6}

/* therapy */
.therapy{top:1328px;height:700px;background:var(--grey-bg)}
.therapy h2{position:absolute;left:75px;top:52px;width:520px;font-size:32px;font-weight:700;line-height:1.3}
.therapy .copy{position:absolute;left:75px;top:142px;width:465px;font-size:11.6px;line-height:1.5}
.btn{position:absolute;display:flex;align-items:center;justify-content:center;gap:12px;color:#fff;border-radius:30px;white-space:nowrap}
.therapy .btn{left:69px;top:465px;width:196px;height:52px;background:var(--blue);font-family:"Libre Caslon Text",Georgia,serif;font-weight:700;font-size:16px}

/* faq */
.faq{top:1990px;height:635px;background:var(--pink-soft)}
.faq h2{position:absolute;left:118px;top:128px;font-size:36px;font-weight:700;letter-spacing:-.5px}
.faq h2 span{color:var(--pink)}
.q{position:absolute;left:113px;font-size:23px;font-weight:500;display:flex;align-items:center;gap:14px;white-space:nowrap}
.q::before{content:"";width:7px;height:7px;border-radius:50%;background:var(--pink)}
.q .sign{color:var(--pink);font-weight:400}
.faq .answer{position:absolute;left:131px;top:242px;width:650px;font-size:17px;line-height:1.25}
.faq .btn{left:130px;top:458px;width:152px;height:45px;background:var(--pink);font-size:14px;font-weight:500}

/* news */
.news{top:2625px;height:553px;background:radial-gradient(circle at 900px 150px,#2C83CF 0%,var(--news) 55%)}
.news h2{position:absolute;left:0;width:1200px;top:46px;text-align:center;color:#fff;font-size:30px;font-weight:700}
.card-text{position:absolute;color:#fff}
.card-text h3{font-size:19px;font-weight:500}
.card-text .lead{font-size:10.5px;font-weight:500;margin-top:8px;line-height:1.25}
.card-text .small{font-size:7.2px;line-height:1.3;margin-top:6px;opacity:.9}
.side-card{position:absolute;left:585px;width:568px;height:143px;border:1.5px solid #d6e6f5}
.news .btn{left:523px;top:477px;width:159px;height:40px;background:var(--blue);font-size:14px;font-weight:500;border:1px solid #3f94d6}

/* help */
.help{top:3178px;height:707px;background:var(--help)}
.help h2{position:absolute;left:0;width:1200px;top:28px;text-align:center;color:#fff;font-size:32px;font-weight:700}
.pill{position:absolute;width:190px;height:54px;border-radius:27px;background:#fff;font-size:20px;display:flex;align-items:center;padding-left:20px;gap:12px;color:#222;white-space:nowrap}
.pill.long{font-size:17px;padding-left:14px;gap:8px}
.pill::before{content:"";width:9px;height:9px;border-radius:50%;background:#c4c4c4;flex:none}

/* contact */
.contact{top:3885px;height:540px;background:#DCDCDC}
.field{position:absolute;background:var(--field);font-size:15px;color:#222;padding:12px 10px}
.contact .send{position:absolute;left:75px;top:415px;width:222px;height:50px;background:var(--blue);color:#fff;font-size:20px;display:flex;align-items:center;justify-content:center}

/* footer */
.site-footer{top:4425px;height:383px;background:var(--footer);color:#fff}
.site-footer .vline{position:absolute;top:0;width:1.5px;height:265px;background:#fff}
.footer-name{position:absolute;left:112px;top:88px;font-size:29px;font-weight:700}
.site-footer h4{position:absolute;font-size:18px;font-weight:500}
.links{position:absolute;left:467px;top:60px;list-style:none;font-size:16.5px}
.links li{height:37px;display:flex;align-items:center;gap:10px}
.links li::before{content:"";width:5px;height:5px;border-radius:50%;background:#fff}
.info{position:absolute;left:855px;display:flex;align-items:center;gap:16px;font-size:15px;white-space:nowrap}
.info svg{flex:none}
.address{position:absolute;left:889px;top:184px;font-size:16px;line-height:1.3}
.bottom-line{position:absolute;left:52px;right:52px;top:310px;height:1.5px;background:#fff}
.copyright{position:absolute;top:325px;left:0;width:1200px;text-align:center;font-size:14px}
.copyright span{display:inline-block;width:1px;height:18px;background:#fff;margin:0 14px;vertical-align:middle}
</style>
</head>
<body>

<header class="hero">
  <div class="hero-bg" role="img" aria-label="Painted scene of a cave opening onto misty green hills with a tree shaped like a human head"></div>
  <div class="brand-text">Logo Here</div>
  <nav class="nav">
    <a class="active" style="left:372px">Home</a>
    <a style="left:478px">About</a>
    <a style="left:584px">Therapy</a>
    <a style="left:706px">FAQ</a>
    <a style="left:797px">Blog</a>
  </nav>
  <div class="contact-btn">Contact Us</div>
  <div class="hero-title serif">
    <h1>RosalindFaber</h1>
    <p>Compassionate Psychotherapy</p>
  </div>
  <svg class="abs" style="left:0;top:540px" width="1200" height="140" viewBox="0 0 1200 140">
    <path d="M0 105 C 250 60, 520 90, 760 80 C 960 70, 1100 40, 1200 20 L1200 140 L0 140 Z" fill="#fff"/>
    <path d="M0 110 C 260 70, 520 125, 780 110 C 960 100, 1100 60, 1200 35" fill="none" stroke="#0677BA" stroke-width="10"/>
  </svg>
</header>

<section class="about">
  <div class="frame" style="left:97px;top:182px;width:90px;height:335px;border-right:none"></div>
  <div class="frame" style="left:500px;top:56px;width:60px;height:20px;border-left:none;border-bottom:none"></div>
  <div class="ph" style="left:146px;top:86px;width:390px;height:396px;background:linear-gradient(180deg,#d8d2ca,#d7a5b4 60%,#d9577f)" role="img" aria-label="Portrait photograph of the therapist in a pink top"></div>
  <div class="ph" style="left:460px;top:10px;width:137px;height:132px;background:linear-gradient(180deg,#e8e5de,#b8b1a4)" role="img" aria-label="Photograph of a group therapy session in a bright room"></div>
  <div class="ph" style="left:77px;top:417px;width:125px;height:133px;background:linear-gradient(135deg,#f0e6da,#c89a76)" role="img" aria-label="Photograph of a hand reaching out to a distressed person"></div>
  <div class="tint" style="left:538px;top:374px;width:50px;height:100px" role="img" aria-label="Light grey dotted accent"></div>
  <div class="tint" style="left:490px;top:480px;width:100px;height:38px" role="img" aria-label="Light grey dotted accent"></div>
  <h2 class="serif">HI , I AM &nbsp;<span>ROSALIND FABER</span></h2>
  <div class="copy">
    <p>I have over 10 years' experience of dealing with addictions. &nbsp;Addictions are often more of a solution to fear and emotional pain. However, eventually the addiction causes more problems. I know recovery is possible with the right support.</p>
    <p>I have also had some twenty years of experience of dealing with mental health issues such as depression, anxiety, complex PTSD and trauma. &nbsp;It is possible to manage these issues and live a full life.<br>I have worked in the voluntary sector as a Harbourline and I am currently a therapist for Calmwell.</p>
  </div>
</section>

<section class="therapy">
  <div class="ph" style="left:697px;top:0;width:503px;height:600px;background:linear-gradient(170deg,#ece7df,#d7c8b6 55%,#b78e6c)" role="img" aria-label="Photograph of a therapist giving a calming head treatment to a client lying down"></div>
  <h2 class="serif">THERAPY WITH &nbsp;&nbsp;<span>ROSALIND FABER</span></h2>
  <div class="copy">
    There are times when the challenges of life can make us feel overwhelmed and isolated, and it may feel difficult to talk about how we feel to those who are closest to us. We go through transitions and crises and experience uncertainty and loss. How we deal with difficulties in life is an important aspect in how we carry on forwards and ultimately who we become as people.<br>
    I offer a range of psychotherapeutic approaches including transactional analysis psychotherapy and relational therapy.<br>
    Through the process of exploration, we enable self-knowledge and self-awareness to help you grow and conquer issues that may previously have been experienced as all-consuming or overwhelming. We will not only look at your problems in the present but also identify the roots of these problems from your past. We will explore how your past experiences may have affected the way you live today and operate within your life in the present and when you become aware and understand this, it is possible for change to take place.
  </div>
  <div class="btn">Read More
    <svg width="10" height="16" viewBox="0 0 10 16"><path d="M2 2l6 6-6 6" fill="none" stroke="#fff" stroke-width="2"/></svg>
  </div>
  <svg class="abs" style="left:0;top:560px" width="1200" height="145" viewBox="0 0 1200 145">
    <path d="M0 115 C 300 20, 850 -10, 1200 125 L1200 145 L0 145 Z" fill="#0677BA"/>
    <path d="M0 145 C 300 45, 850 20, 1200 145 Z" fill="#F9D9EA"/>
  </svg>
</section>

<section class="faq">
  <div class="ph" style="left:830px;top:175px;width:370px;height:460px;background:linear-gradient(180deg,var(--pink-mid) 0%,#EE8ABF 50%,var(--pink-soft) 100%)" role="img" aria-label="Photograph of a pink gerbera flower on a long stem"></div>
  <h2 class="serif">COMMON <span>QUESTION</span></h2>
  <div class="q" style="top:198px">How long will I need therapy for ? <span class="sign">—</span></div>
  <p class="answer">Therapy can last anywhere from one session to several months or even years. It all depends on what you want and need. Some people come to therapy with a very specific problem they need to solve and might find that one or two sessions is sufficient.</p>
  <div class="q" style="top:341px">How long are the sessions? <span class="sign">+</span></div>
  <div class="q" style="top:391px">How much is each session? <span class="sign">+</span></div>
  <div class="btn">READ MORE
    <svg width="8" height="12" viewBox="0 0 8 12"><path d="M2 1l5 5-5 5" fill="none" stroke="#fff" stroke-width="1.6"/></svg>
  </div>
</section>

<section class="news">
  <h2 class="serif">LATEST NEWS</h2>
  <div class="ph" style="left:93px;top:125px;width:479px;height:317px;background:linear-gradient(180deg,#8d8a84,#5c5852 55%,#2a2723)" role="img" aria-label="Photograph of a worried child while parents argue behind"></div>
  <div class="card-text" style="left:116px;top:310px;width:340px">
    <h3>Family Issue</h3>
    <p class="lead">Trauma and the bears – a fable<br>Once upon a time there were humans on the savannah. It was a dangerous world.</p>
    <p class="small">First food, we need to find shelter, water and warmth. We need each other to feel safe, and we learn together how to survive.</p>
  </div>

  <div class="side-card" style="top:125px"></div>
  <div class="ph" style="left:585px;top:125px;width:233px;height:143px;background:linear-gradient(135deg,#8a8a8a,#3e3e3e)" role="img" aria-label="Photograph of an upset couple sitting back to back"></div>
  <div class="card-text" style="left:839px;top:148px;width:300px">
    <h3>Relationship Issue</h3>
    <p class="lead">So we're humans on the savannah. We're not bigger or faster than other predators,</p>
    <p class="small">Hypervigilance might stop us sleeping at night. It might make us jittery and anxious, but it keeps a nervous human alive. Our tribe is everything.</p>
  </div>

  <div class="side-card" style="top:303px"></div>
  <div class="ph" style="left:585px;top:303px;width:233px;height:143px;background:linear-gradient(135deg,#d8dde3,#8c96a3)" role="img" aria-label="Illustration of a stressed man holding his head with scribbled thoughts"></div>
  <div class="card-text" style="left:839px;top:326px;width:300px">
    <h3>Bussiness Issue</h3>
    <p class="lead">So we're humans on the savannah and today we're down by the river looking for berries</p>
    <p class="small">Hypervigilance might stop us sleeping at night, but a nervous human is a living one. We communicate, we cooperate, we survive.</p>
  </div>

  <div class="btn">READ MORE
    <svg width="8" height="12" viewBox="0 0 8 12"><path d="M2 1l5 5-5 5" fill="none" stroke="#fff" stroke-width="1.6"/></svg>
  </div>
</section>

<section class="help">
  <h2 class="serif">WHAT WE CAN HELP WITH</h2>
  <div class="pill" style="left:180px;top:118px">Addiction</div>
  <div class="pill" style="left:508px;top:114px">Anger</div>
  <div class="pill" style="left:836px;top:118px">Anxiety</div>
  <div class="pill" style="left:180px;top:200px">Bulling</div>
  <div class="pill long" style="left:508px;top:202px">Career Changes</div>
  <div class="pill" style="left:836px;top:202px">Breakdown</div>
  <div class="pill" style="left:180px;top:285px">Depression</div>
  <div class="pill" style="left:508px;top:285px">Feeling Alone</div>
  <div class="pill" style="left:836px;top:285px">Health Issue</div>
  <div class="pill" style="left:180px;top:370px">Fear</div>
  <div class="pill" style="left:508px;top:370px">Identity Issue</div>
  <div class="pill long" style="left:836px;top:372px">Negative Thinking</div>
  <div class="pill" style="left:180px;top:455px">HIV</div>
  <div class="pill" style="left:508px;top:453px">Psychosis</div>
  <div class="pill" style="left:836px;top:457px">LGBT Issue</div>
  <div class="pill long" style="left:180px;top:538px">Loss Of Meaning</div>
  <div class="pill" style="left:508px;top:538px">Sexual Abuse</div>
  <div class="pill" style="left:836px;top:540px">Sexuality</div>
  <svg class="abs" style="left:1132px;top:282px" width="40" height="74" viewBox="0 0 40 74"><path d="M4 3l32 34-32 34" fill="none" stroke="#fff" stroke-width="3"/></svg>
</section>

<section class="contact">
  <div class="field" style="left:75px;top:47px;width:303px;height:48px">First Name:</div>
  <div class="field" style="left:398px;top:47px;width:304px;height:48px">Last Name:</div>
  <div class="field" style="left:75px;top:103px;width:303px;height:48px">Contact Num:</div>
  <div class="field" style="left:398px;top:103px;width:304px;height:48px">E-Mail:</div>
  <div class="field" style="left:75px;top:160px;width:627px;height:238px">Leave a message:</div>
  <div class="send">Send Messge</div>
  <div class="ph" style="left:750px;top:33px;width:378px;height:450px;background:linear-gradient(150deg,#dfe3e6,#9aa3aa 55%,#3a4147)" role="img" aria-label="Photograph of hands typing on a laptop holding a red phone"></div>
</section>

<footer class="site-footer">
  <div class="vline" style="left:368px"></div>
  <div class="vline" style="left:715px"></div>
  <div class="footer-name">LOGO HERE</div>
  <h4 style="left:483px;top:27px">Quick Links</h4>
  <ul class="links">
    <li>Home</li><li>About</li><li>Therapy</li><li>FAQ</li><li>Blog</li><li>Contact Us</li>
  </ul>
  <h4 style="left:853px;top:35px">Contact Us</h4>
  <div class="info" style="top:69px">
    <svg width="18" height="18" viewBox="0 0 18 18" fill="none" stroke="#fff" stroke-width="1.4"><circle cx="9" cy="9" r="7.5"/><ellipse cx="9" cy="9" rx="3.2" ry="7.5"/><path d="M1.5 9h15"/></svg>
    www.rosalindfaber.co.uk</div>
  <div class="info" style="top:102px">
    <svg width="18" height="14" viewBox="0 0 18 14" fill="none" stroke="#fff" stroke-width="1.4"><rect x="1" y="1" width="16" height="12"/><path d="M1 1l8 7 8-7"/></svg>
    rosalindfaber@counselling.co.uk</div>
  <div class="info" style="top:133px">
    <svg width="16" height="16" viewBox="0 0 16 16"><path d="M3 1l3 3-1.5 2c1 2 3 4 5 5l2-1.5 3 3-2 2C7 14 2 9 1 3z" fill="#fff"/></svg>
    07700 900418</div>
  <div class="info" style="top:184px">
    <svg width="14" height="19" viewBox="0 0 14 19"><path d="M7 0C3 0 0 3 0 7c0 5 7 12 7 12s7-7 7-12c0-4-3-7-7-7z" fill="#fff"/><circle cx="7" cy="7" r="2.6" fill="#1068B3"/></svg>
  </div>
  <div class="address">Alder Community Centre<br><span style="display:block;height:8px"></span>27 Linden Road<br>East Twickenham<br>TW1 4QX</div>
  <div class="bottom-line"></div>
  <div class="copyright">@ 2021Copyright<span></span>All Rights Reserved</div>
</footer>

</body>
</html>
```